Marcus Delwyn-Hart Finance

Need a personal website advertising Equipment Finance,Business Finance,Commercial Finance, Construction Finance, Bridging Finance. Similar websites are www.qorvimark.com.au / www.talsbrio.com.au / www.zpk7.com.au /wwwlemberwick.com.au

Target Market(s)

Business People

Industry/Entity Type

Business

Number of Pages Required

3 page

Font styles to use
Serif
Sans Serif

Requirements
Must have
• All i want is a simple corporate looking website advertising Equipment Finance, Commercial Finance, Construction Finance, Business Finance, Bridging Finance,

```html
<!DOCTYPE html>
<html lang="en">
<head>
<meta charset="utf-8">
<title>Marcus Delwyn-Hart Finance</title>
<link href="https://fonts.googleapis.com/css2?family=Roboto:wght@300;400;500;700&family=Roboto+Condensed:wght@400;700&display=swap" rel="stylesheet">
<style>
:root{
  --navy:#0b2d5b;
  --navy-dark:#08244a;
  --sky:#00aeef;
  --sky-soft:#e9f4fd;
  --grey-text:#8a8f96;
  --body-text:#555a60;
  --line:#e3e6ea;
  --footer-bg:#e2e6e9;
  --badge:#d5dbe1;
  --white:#ffffff;
}
*{box-sizing:border-box;margin:0;padding:0}
html,body{width:1200px;height:2476px;overflow:hidden}
body{font-family:"Roboto",Arial,sans-serif;color:var(--body-text);background:var(--white);position:relative}
.wrap{width:900px;margin:0 auto;position:relative}

/* top bar */
.topbar{height:38px;background:#f3f8fd;border-bottom:1px solid var(--line)}
.topbar .wrap{display:flex;height:38px;align-items:stretch}
.topbar-link{font-size:11px;color:var(--navy);padding:0 12px;display:flex;align-items:center;border-left:1px solid var(--line);border-right:1px solid var(--line)}
.social-slot{width:38px;display:flex;align-items:center;justify-content:center;border-right:1px solid var(--line)}
.social-slot span{width:14px;height:14px;border-radius:50%;background:var(--navy)}
.quick-tab{margin-left:auto;background:var(--navy);color:#fff;font-size:12px;width:118px;display:flex;align-items:center;justify-content:center;border-radius:6px 6px 0 0;margin-top:6px;margin-right:20px}

/* header */
.header{height:79px}
.header .wrap{display:flex;align-items:center;height:79px}
.brand{font-weight:700;color:var(--navy);font-size:17px;line-height:19px;width:170px}
.main-menu{display:flex;gap:20px;margin-left:24px;font-size:11.5px;color:var(--navy)}
.main-menu .active{color:var(--sky);border-bottom:1px solid var(--sky);padding-bottom:4px}
.header-phone{margin-left:auto;font-size:24px;color:var(--navy);font-weight:400;margin-right:-2px}

/* service nav */
.service-nav{height:37px;background:var(--sky)}
.service-nav .wrap{display:flex;gap:30px;height:37px;align-items:center;font-size:13px;color:#fff}

/* hero */
.hero{height:376px;position:relative;background:linear-gradient(90deg,#bcd3e3 0%,#d9e8f2 30%,#e6f0f6 60%,#cfe0ec 100%);overflow:hidden}
.hero-photo{position:absolute;right:0;top:0;width:320px;height:376px;background:linear-gradient(180deg,#cfe1ee 0%,#6d7f94 45%,#1c2633 100%)}
.hero-text{position:absolute;left:162px;top:88px}
.hero-title{font-family:"Roboto Condensed",Arial,sans-serif;font-weight:700;font-size:37px;color:var(--navy);letter-spacing:.5px}
.hero-sub{font-size:21px;font-weight:400;color:var(--navy);line-height:27px;margin-top:6px;text-transform:uppercase}
.btn-navy{display:inline-flex;align-items:center;gap:10px;background:var(--navy);color:#fff;font-size:12.5px;padding:0 22px}
.hero .btn-navy{position:absolute;left:170px;top:221px;height:37px;width:150px;justify-content:center}

/* welcome */
.welcome{height:208px;text-align:center;padding-top:34px}
.welcome h1{font-weight:300;font-size:37px;color:var(--navy)}
.welcome p{width:870px;margin:20px auto 0;font-size:11.6px;line-height:15px;color:#555}

/* services */
.services{height:547px;background:var(--sky-soft);padding-top:80px}
.service-grid{display:grid;grid-template-columns:repeat(3,1fr);gap:2px;width:900px;margin:0 auto;background:var(--line)}
.service-card{background:#fff;height:191px;text-align:center;padding-top:20px}
.service-card svg{display:block;margin:0 auto}
.service-card h3{font-weight:400;font-size:14.5px;color:#222;margin-top:10px}
.service-card .rule{width:36px;height:2px;background:var(--sky);margin:9px auto 12px}
.service-card p{font-size:10.6px;color:var(--grey-text);line-height:13px;width:200px;margin:0 auto}
.service-cta{background:var(--sky);color:#fff;padding-top:26px}
.service-cta .cta-label{font-size:14px}
.service-cta .cta-phone{font-size:23px;margin-top:12px}
.service-cta p{color:#fff;font-size:11px;margin-top:12px;width:230px}
.service-cta .btn-navy{height:34px;width:146px;justify-content:center;margin-top:14px;font-size:12px}

/* meet */
.meet{height:385px;position:relative}
.meet-portrait{position:absolute;left:165px;top:-31px;width:240px;height:416px;background:linear-gradient(180deg,#d7dbdf 0%,#7b828c 40%,#2a2f37 100%)}
.meet-bar{position:absolute;left:424px;top:13px;width:627px;height:44px;background:var(--navy);border-left:5px solid var(--sky);color:#fff;font-size:17px;padding-left:16px;display:flex;align-items:center}
.meet-body{position:absolute;left:428px;top:79px;width:455px}
.meet-lead{color:var(--sky);font-size:15.5px}
.meet-sub{color:#222;font-size:16px;margin-top:6px}
.meet-body p{font-size:12px;line-height:21px;color:#555;margin-top:6px}
.meet-body .btn-sky{display:inline-flex;align-items:center;gap:8px;background:var(--sky);color:#fff;font-size:13px;height:35px;padding:0 20px;margin-top:16px}
.achievements{position:absolute;left:892px;top:75px;width:159px;border-left:1px solid var(--line);height:250px;text-align:center}
.achievements h4{font-weight:500;font-size:16px;color:var(--navy)}
.achievements .rule{width:120px;height:1px;background:var(--line);margin:8px auto 0}
.badge-placeholder{width:72px;height:72px;background:var(--badge);margin:28px auto 0}
.badge-placeholder.round{border-radius:50%}
.badge-placeholder + .badge-placeholder{margin-top:18px}
.meet-line{position:absolute;left:150px;right:149px;bottom:0;height:1px;background:var(--line)}

/* articles */
.articles{display:grid;grid-template-columns:repeat(3,300px);width:900px;margin:59px auto 0;gap:0}
.article{text-align:center}
.article-photo{height:223px;margin:0 1px}
.article h3{font-weight:400;font-size:15px;color:#222;margin-top:12px}
.article .rule{width:70px;height:1px;background:var(--sky);margin:8px auto 8px}
.article p{font-size:10.8px;color:var(--grey-text);line-height:13px;width:250px;margin:0 auto}
.article a{display:block;color:var(--sky);font-size:11px;margin-top:4px;text-decoration:none}

/* partners */
.partners{width:900px;margin:62px auto 0;border-top:1px solid var(--line);height:91px;display:flex;align-items:center;justify-content:space-between;padding:0 30px}
.partner{font-weight:700;font-size:14px;color:var(--navy);display:flex;align-items:center;gap:6px}
.partner i{width:9px;height:9px;background:var(--sky);display:inline-block}

/* footer */
.footer{height:187px;background:var(--footer-bg)}
.footer .wrap{display:flex;padding-top:38px}
.footer ul{list-style:none;font-size:10.6px;color:var(--navy);line-height:22.5px}
.footer-services{width:265px;padding-left:20px}
.footer-pages{width:175px}
.subscribe h5{font-weight:400;font-size:11px;color:var(--navy)}
.subscribe-row{display:flex;gap:18px;margin-top:8px}
.subscribe-input{width:255px;height:36px;background:#fff;font-size:11px;color:#888;padding-left:10px;display:flex;align-items:center}
.subscribe-btn{width:144px;height:36px;background:var(--sky);color:#fff;font-size:14px;display:flex;align-items:center;justify-content:center}
.footer-social{display:flex;gap:8px;margin-top:12px}
.footer-social span{width:23px;height:23px;border-radius:50%;background:var(--navy)}
.copyright{text-align:center;font-size:10px;color:#333;padding-top:28px}
</style>
</head>
<body>

<div class="topbar">
  <div class="wrap">
    <div class="topbar-link">Contact Us</div>
    <div class="social-slot"><span></span></div>
    <div class="social-slot"><span></span></div>
    <div class="social-slot"><span></span></div>
    <div class="social-slot"><span></span></div>
    <div class="quick-tab">QUICK QUOTE</div>
  </div>
</div>

<header class="header">
  <div class="wrap">
    <div class="brand">Marcus Delwyn-Hart<br>Finance</div>
    <nav class="main-menu">
      <span class="active">HOME</span><span>ABOUT MARCUS</span><span>CONTACT</span>
    </nav>
    <div class="header-phone">555-318-4720</div>
  </div>
</header>

<nav class="service-nav">
  <div class="wrap">
    <span>Equipment Finance</span><span>Commercial Finance</span><span>Construction Finance</span><span>Business Finance</span><span>Bridging Finance</span>
  </div>
</nav>

<section class="hero" role="img" aria-label="Blurred city office backdrop with glass tower">
  <div class="hero-photo" role="img" aria-label="Smiling businessman in a suit offering a handshake"></div>
  <div class="hero-text">
    <h2 class="hero-title">FINANCE SOLUTIONS</h2>
    <div class="hero-sub">Lorem ipsum dolor sit amet, consectetur<br>adipiscing elit. Sed euismod odio</div>
  </div>
  <div class="btn-navy">
    <svg width="16" height="8" viewBox="0 0 16 8"><path d="M0 4h14M11 1l3 3-3 3" stroke="#fff" stroke-width="1.4" fill="none"/></svg>
    GET QUOTE
  </div>
</section>

<section class="welcome">
  <h1>Welcome</h1>
  <p>Lorem ipsum dolor sit amet, consectetur adipiscing elit. Sed vel semper risus, id consequat mauris. Curabitur sit amet accumsan est, at sollicitudin nunc. Nullam semper at nulla eget dictum. Fusce mollis laoreet mattis. Suspendisse eget sagittis dolor. Phasellus facilisis quam dolor. Donec ac odio et justo ultricies efficitur at pharetra sem. Sed blandit, velit in tristique volutpat, libero mi pellentesque dolor, sed porta eros lacus ut odio. Etiam tempus ipsum justo, eget faucibus augue dignissim ac. Phasellus sit amet vulputate felis. Proin ligula ante, porta id posuere in, finibus sit amet mauris.</p>
</section>

<section class="services">
  <div class="service-grid">
    <div class="service-card">
      <svg width="52" height="44" viewBox="0 0 52 44"><rect x="8" y="14" width="20" height="18" fill="#00aeef"/><rect x="28" y="4" width="3" height="28" fill="#00aeef"/><rect x="31" y="28" width="14" height="3" fill="#00aeef"/><circle cx="13" cy="36" r="5" fill="#00aeef"/><circle cx="25" cy="36" r="5" fill="#00aeef"/></svg>
      <h3>Equipment Finance</h3><div class="rule"></div>
      <p>Lorem ipsum dolor sit amet, consectetur adipiscing elit. Sed euismod odio vitae orci tempor, eget egestas nunc condimentum.</p>
    </div>
    <div class="service-card">
      <svg width="52" height="44" viewBox="0 0 52 44"><rect x="8" y="28" width="7" height="12" fill="#00aeef"/><rect x="18" y="22" width="7" height="18" fill="#00aeef"/><rect x="28" y="25" width="7" height="15" fill="#00aeef"/><rect x="38" y="14" width="7" height="26" fill="#00aeef"/><path d="M8 22l10-8 10 4 14-12" stroke="#0b2d5b" stroke-width="2" fill="none"/></svg>
      <h3>Commercial Finance</h3><div class="rule"></div>
      <p>Lorem ipsum dolor sit amet, consectetur adipiscing elit. Sed euismod odio vitae orci tempor, eget egestas nunc condimentum.</p>
    </div>
    <div class="service-card">
      <svg width="52" height="44" viewBox="0 0 52 44"><rect x="14" y="4" width="24" height="36" fill="none" stroke="#00aeef" stroke-width="3"/><rect x="19" y="10" width="5" height="5" fill="#00aeef"/><rect x="28" y="10" width="5" height="5" fill="#00aeef"/><rect x="19" y="19" width="5" height="5" fill="#00aeef"/><rect x="28" y="19" width="5" height="5" fill="#00aeef"/><rect x="23" y="30" width="6" height="10" fill="#00aeef"/></svg>
      <h3>Construction Finance</h3><div class="rule"></div>
      <p>Lorem ipsum dolor sit amet, consectetur adipiscing elit. Sed euismod odio vitae orci tempor, eget egestas nunc condimentum.</p>
    </div>
    <div class="service-card">
      <svg width="52" height="44" viewBox="0 0 52 44"><path d="M4 18l12-8 10 6 10-6 12 8-8 10-14 8-14-8z" fill="#00aeef"/></svg>
      <h3>Business Finance</h3><div class="rule"></div>
      <p>Lorem ipsum dolor sit amet, consectetur adipiscing elit. Sed euismod odio vitae orci tempor, eget egestas nunc condimentum.</p>
    </div>
    <div class="service-card">
      <svg width="52" height="44" viewBox="0 0 52 44"><rect x="6" y="8" width="30" height="28" fill="none" stroke="#00aeef" stroke-width="3"/><rect x="6" y="8" width="30" height="7" fill="#00aeef"/><rect x="11" y="19" width="5" height="4" fill="#00aeef"/><rect x="19" y="19" width="5" height="4" fill="#00aeef"/><rect x="27" y="19" width="5" height="4" fill="#00aeef"/><rect x="30" y="28" width="18" height="12" fill="#fff" stroke="#00aeef" stroke-width="2"/><circle cx="39" cy="34" r="3" fill="#00aeef"/></svg>
      <h3>Bridging Finance</h3><div class="rule"></div>
      <p>Lorem ipsum dolor sit amet, consectetur adipiscing elit. Sed euismod odio vitae orci tempor, eget egestas nunc condimentum.</p>
    </div>
    <div class="service-card service-cta">
      <div class="cta-label">For More Info Call:</div>
      <div class="cta-phone">555-318-4720</div>
      <p>Lorem ipsum dolor sit amet, consectetur adipiscing elit.</p>
      <div class="btn-navy">QUICK QUOTE</div>
    </div>
  </div>
</section>

<section class="meet">
  <div class="meet-portrait" role="img" aria-label="Portrait of the advisor standing in a dark suit"></div>
  <div class="meet-bar">Meet Marcus Delwyn-Hart</div>
  <div class="meet-body">
    <div class="meet-lead">Proin id vestibulum libero.</div>
    <div class="meet-sub">Morbi vel eros pulvinar aliquam fermentum convallis risus.</div>
    <p>Lorem ipsum dolor sit amet, consectetur adipiscing elit. In faucibus pellentesque massa, non scelerisque arcu dapibus in. Lorem ipsum dolor sit amet, consectetur adipiscing elit. Nullam gravida, libero eget vestibulum ultricies, odio lacus lobortis lorem, fringilla vehicula nunc dolor ut turpis. Donec sit amet nibh luctus, imperdiet metus eget, bibendum sapien. Vestibulum porta, diam nec volutpat dignissim, massa diam dignissim arcu, dictum auctor risus leo varius purus. Suspendisse gravida vehicula orci in malesuada. Aliquam sagittis lacinia diam ut rutrum. Vivamus placerat justo et mauris imperdiet tristique.</p>
    <div class="btn-sky">
      <svg width="7" height="8" viewBox="0 0 7 8"><path d="M0 0l7 4-7 4z" fill="#fff"/></svg>
      Full Bio
    </div>
  </div>
  <aside class="achievements">
    <h4>Achievements</h4>
    <div class="rule"></div>
    <div class="badge-placeholder round" role="img" aria-label="Industry award badge"></div>
    <div class="badge-placeholder" role="img" aria-label="Industry award badge"></div>
  </aside>
  <div class="meet-line"></div>
</section>

<section class="articles">
  <article class="article">
    <div class="article-photo" role="img" aria-label="Person in a hoodie working on a laptop" style="background:linear-gradient(160deg,#eceff2,#b9bfc6 60%,#dfe3e7)"></div>
    <h3>In aliquam tortor et nunc maximus</h3><div class="rule"></div>
    <p>Lorem ipsum dolor sit amet, consectetur adipiscing elit. Sed euismod odio vitae orci tempor, eget egestas nunc condimentum.</p>
    <a>- Read more</a>
  </article>
  <article class="article">
    <div class="article-photo" role="img" aria-label="Overhead view of colleagues reviewing paperwork at a laptop" style="background:linear-gradient(160deg,#c9d6e2,#8ea3b8 55%,#e6e9ee)"></div>
    <h3>In aliquam tortor et nunc maximus</h3><div class="rule"></div>
    <p>Lorem ipsum dolor sit amet, consectetur adipiscing elit. Sed euismod odio vitae orci tempor, eget egestas nunc condimentum.</p>
    <a>- Read more</a>
  </article>
  <article class="article">
    <div class="article-photo" role="img" aria-label="Support team wearing headsets in an office" style="background:linear-gradient(160deg,#f0f2f4,#c3cad2 55%,#e8ecef)"></div>
    <h3>In aliquam tortor et nunc maximus</h3><div class="rule"></div>
    <p>Lorem ipsum dolor sit amet, consectetur adipiscing elit. Sed euismod odio vitae orci tempor, eget egestas nunc condimentum.</p>
    <a>- Read more</a>
  </article>
</section>

<section class="partners">
  <span class="partner">Arvena</span>
  <span class="partner">Kestrel Bank</span>
  <span class="partner">Norvale</span>
  <span class="partner"><i></i>Tamsford</span>
  <span class="partner">Brightway Funding</span>
  <span class="partner">Saltmere</span>
  <span class="partner">Lumio</span>
</section>

<footer class="footer">
  <div class="wrap">
    <ul class="footer-services">
      <li>EQUIPMENT FINANCE</li><li>COMMERCIAL FINANCE</li><li>CONSTRUCTION FINANCE</li><li>BUSINESS FINANCE</li><li>BRIDGING FINANCE</li>
    </ul>
    <ul class="footer-pages">
      <li>HOME</li><li>ABOUT MARCUS</li><li>CONTACT</li>
    </ul>
    <div class="subscribe">
      <h5>SUBSCRIBE FOR THE LATEST NEWS</h5>
      <div class="subscribe-row">
        <div class="subscribe-input">Enter Your Email</div>
        <div class="subscribe-btn">SUBSCRIBE</div>
      </div>
      <div class="footer-social"><span></span><span></span><span></span><span></span></div>
    </div>
  </div>
</footer>

<div class="copyright">Copyright 2017 delwynhart.com All Rights Reserved.</div>

</body>
</html>
```